Business Card Design

Lintel Comms is a public relations consultancy service for the self build, home refurbishment and home improvement market.
It represents everything about 'home' so envisage logo featuring maybe roof pitch over the 'A' of Lintel. Colour/font undecided.

Industry/Entity Type

Home Improvement

Contact Information for Business Card

Fenella Coxworth
fenella@lintelcomms.co.uk
Telephone Direct: 0788 142 6597

```html
<!DOCTYPE html>
<html lang="en">
<head>
<meta charset="utf-8">
<title>Lintel Comms – Business Card</title>
<link rel="stylesheet" href="https://fonts.googleapis.com/css2?family=Saira:wght@600&family=Fira+Sans:wght@300;400&display=swap">
<style>
  :root {
    --card-paper: #e4e8e9;
    --card-paper-light: #eef1f2;
    --brand-maroon: #5a1408;
    --rule-wood: #7a2a12;
    --wood-dark: #6e1d0b;
    --wood-mid: #9a3417;
    --wood-light: #b2481f;
    --name-white: #fbf4ef;
    --contact-ink: #3a1a12;
  }
  html, body {
    margin: 0;
    padding: 0;
    overflow: hidden;
    background: #ffffff;
  }
  .business-card {
    position: relative;
    width: 1200px;
    height: 668px;
    overflow: hidden;
    background: radial-gradient(ellipse at 50% 35%, var(--card-paper-light), var(--card-paper) 75%);
  }
  .vertical-rule {
    position: absolute;
    left: 84px;
    width: 8px;
    background: linear-gradient(90deg, var(--wood-dark), var(--wood-light) 50%, var(--wood-dark));
  }
  .vertical-rule--upper { top: 0; height: 430px; }
  .vertical-rule--lower { top: 540px; height: 128px; }
  .wood-band {
    position: absolute;
    left: 0;
    top: 430px;
    width: 1200px;
    height: 110px;
    background:
      linear-gradient(180deg, rgba(0,0,0,0.25) 0, rgba(0,0,0,0) 8px, rgba(0,0,0,0) 100px, rgba(0,0,0,0.25) 110px),
      linear-gradient(90deg, var(--wood-mid), var(--wood-light) 22%, var(--wood-dark) 45%, var(--wood-mid) 68%, var(--wood-light) 85%, var(--wood-mid));
  }
  .company-name {
    position: absolute;
    left: 300px;
    top: 140px;
    margin: 0;
    font-family: "Saira", sans-serif;
    font-weight: 600;
    font-size: 88px;
    letter-spacing: 3px;
    line-height: 1;
    color: var(--brand-maroon);
  }
  .person-name {
    position: absolute;
    left: 0;
    right: 0;
    top: 452px;
    margin: 0;
    text-align: center;
    padding-right: 24px;
    font-family: "Fira Sans", sans-serif;
    font-weight: 300;
    font-size: 56px;
    line-height: 1.2;
    color: var(--name-white);
  }
  .contact-line {
    position: absolute;
    left: 210px;
    top: 596px;
    margin: 0;
    font-family: "Fira Sans", sans-serif;
    font-weight: 400;
    font-size: 22px;
    color: var(--contact-ink);
    white-space: nowrap;
  }
  .contact-line .contact-email { margin-left: 44px; }
</style>
</head>
<body>
  <main class="business-card">
    <div class="vertical-rule vertical-rule--upper"></div>
    <div class="wood-band" role="img" aria-label="Horizontal band of red-brown polished wood grain"></div>
    <div class="vertical-rule vertical-rule--lower"></div>

    <h1 class="company-name">Lintel Comms</h1>
    <p class="person-name">Fenella Coxworth</p>
    <p class="contact-line">
      <span class="contact-phone">Telephone Direct: 0788 142 6597</span>
      <span class="contact-email">fenella@lintelcomms.co.uk</span>
    </p>
  </main>
</body>
</html>
```